Overhead Menu Design for a Matcha Business

Hello, we are a Matcha startup and we need a designer to design an overhead menu for the next farmers market. Each menu item is to stand alone, similar to a square poster for each item (refer to rough sketches for visual explanation). Requirements:- Title of each item should be large enough to be read from a distance.- Leave a space on the bottom of each square poster so we can hand write the prices- Drawings should be simple/minimalistic (refer to inspirations)Total menu items: 6Matcha Latte - Iced (Flavors include Original, and Coconut)Matcha Latte - HotMatcha Shot - Iced (Flavors include Original, Peach, Green Apple, and Passion Fruit)Matcha Shot - HotMatcha Ice CreamMatcha BrownieWe look forward to working with you!

Target Market(s)

Customers at an outdoor market

Colors
acd036
cadf82
9bcb3b

Requirements
Must have
• Minimal + Modern + Simple

```html
<!DOCTYPE html>
<html lang="en">
<head>
<meta charset="utf-8">
<title>Matcha Menu Cards</title>
<link href="https://fonts.googleapis.com/css2?family=Fira+Sans+Extra+Condensed:wght@600;700&display=swap" rel="stylesheet">
<style>
  :root {
    --page: #eeeeec;
    --card: #9bc23c;
    --card-line: #cadf82;
    --pale: #cadf82;
    --white: #ffffff;
  }
  * { box-sizing: border-box; margin: 0; padding: 0; }
  html, body { width: 1200px; height: 1000px; overflow: hidden; }
  body {
    background: var(--page);
    font-family: "Fira Sans Extra Condensed", "Arial Narrow", sans-serif;
    position: relative;
  }
  .menu-card {
    position: absolute;
    width: 280px;
    height: 280px;
    background: var(--card);
    box-shadow: 2px 3px 6px rgba(0,0,0,0.25);
  }
  .menu-card::before {
    content: "";
    position: absolute;
    inset: 8px;
    border: 1.5px solid var(--card-line);
    border-radius: 10px;
  }
  .item-title {
    position: absolute;
    left: 0; right: 0;
    text-align: center;
    color: var(--white);
    font-weight: 700;
    font-size: 27px;
    letter-spacing: 1px;
    line-height: 1;
  }
  .item-style {
    position: absolute;
    left: 0; right: 0;
    padding-left: 4px;
    text-align: center;
    color: var(--pale);
    font-weight: 700;
    font-size: 20px;
    letter-spacing: 4px;
    line-height: 1;
  }
  .item-icon {
    position: absolute;
    left: 50%;
    transform: translateX(-50%);
    background: var(--pale);
    border-radius: 10px;
  }
  .flavors {
    position: absolute;
    left: 0; right: 0;
    text-align: center;
    color: var(--white);
    font-weight: 600;
    line-height: 1.1;
  }
  .flavors-label { font-size: 14px; letter-spacing: 2.5px; padding-left: 2.5px; }
  .flavors-list { font-size: 14px; letter-spacing: 1px; }
  .flavors-list.compact { font-size: 12.5px; letter-spacing: 0.5px; }
  .price-space {
    position: absolute;
    left: 22px; right: 22px;
    height: 36px;
    background: var(--white);
    border-radius: 8px;
  }
</style>
</head>
<body>

  <section class="menu-card" style="left:298px; top:43px;">
    <h2 class="item-title" style="top:18px;">MATCHA LATTE</h2>
    <p class="item-style" style="top:44px;">ICED</p>
    <div class="item-icon" role="img" aria-label="Iced drink glass with straw and ice cubes" style="top:70px; width:72px; height:106px;"></div>
    <div class="flavors" style="top:190px;">
      <p class="flavors-label">FLAVORS:</p>
      <p class="flavors-list">•Original &nbsp;•Coconut</p>
    </div>
    <div class="price-space" style="top:228px;"></div>
  </section>

  <section class="menu-card" style="left:620px; top:43px;">
    <h2 class="item-title" style="top:20px;">MATCHA SHOT</h2>
    <p class="item-style" style="top:47px;">ICED</p>
    <div class="item-icon" role="img" aria-label="Iced shot glass with straw and ice cubes" style="top:73px; width:72px; height:102px;"></div>
    <div class="flavors" style="top:182px;">
      <p class="flavors-label">FLAVORS:</p>
      <p class="flavors-list compact">•Original •Peach</p>
      <p class="flavors-list compact">•Green Apple •Passion Fruit</p>
    </div>
    <div class="price-space" style="top:228px;"></div>
  </section>

  <section class="menu-card" style="left:298px; top:357px;">
    <h2 class="item-title" style="top:18px;">MATCHA LATTE</h2>
    <p class="item-style" style="top:46px;">HOT</p>
    <div class="item-icon" role="img" aria-label="Steaming latte cup" style="top:86px; width:106px; height:92px;"></div>
    <div class="flavors" style="top:188px;">
      <p class="flavors-label">FLAVORS:</p>
      <p class="flavors-list">•Original &nbsp;•Coconut</p>
    </div>
    <div class="price-space" style="top:226px;"></div>
  </section>

  <section class="menu-card" style="left:617px; top:357px;">
    <h2 class="item-title" style="top:27px;">MATCH ICE CREAM</h2>
    <div class="item-icon" role="img" aria-label="Ice cream cone with one scoop" style="top:70px; width:50px; height:140px;"></div>
    <div class="price-space" style="top:226px;"></div>
  </section>

  <section class="menu-card" style="left:298px; top:675px;">
    <h2 class="item-title" style="top:20px;">MATCHA SHOT</h2>
    <p class="item-style" style="top:48px;">HOT</p>
    <div class="item-icon" role="img" aria-label="Small steaming shot cup" style="top:84px; width:72px; height:82px;"></div>
    <div class="flavors" style="top:190px;">
      <p class="flavors-label">FLAVORS:</p>
      <p class="flavors-list">•Original &nbsp;•Coconut</p>
    </div>
    <div class="price-space" style="top:227px;"></div>
  </section>

  <section class="menu-card" style="left:617px; top:675px;">
    <h2 class="item-title" style="top:34px;">MATCHA BROWNIE</h2>
    <div class="item-icon" role="img" aria-label="Square brownie slice" style="top:90px; width:114px; height:66px;"></div>
    <div class="price-space" style="top:227px;"></div>
  </section>

</body>
</html>
```